Surviving Domestic Violence Flyer

I need a flyer that "POPS" to attract participants for my research project. I have added the important information on my draft flyer.

```html
<!DOCTYPE html>
<html lang="en">
<head>
<meta charset="utf-8">
<title>Survivor Resources Study Flyer</title>
<link rel="stylesheet" href="https://fonts.googleapis.com/css2?family=Oswald:wght@400;500;700&family=Open+Sans:wght@400;600;700&display=swap">
<style>
  :root {
    --bg-dark: #3a3e3f;
    --bg-deep: #2c3031;
    --photo-light: #8a9698;
    --photo-mid: #5d6a6d;
    --white: #ffffff;
    --orange: #ee6a2c;
    --bullet-text: #c4c4b8;
    --body-text: #1e2121;
    --teal: #6fb8ab;
    --tab-line: #c8653a;
  }
  html, body {
    margin: 0;
    padding: 0;
    width: 927px;
    height: 1200px;
    overflow: hidden;
    background: var(--bg-dark);
  }
  .flyer {
    position: relative;
    width: 927px;
    height: 1200px;
    overflow: hidden;
    background: var(--bg-dark);
    font-family: "Open Sans", Arial, sans-serif;
  }
  .hero-photo {
    position: absolute;
    left: 0;
    top: 0;
    width: 927px;
    height: 590px;
    background:
      radial-gradient(ellipse 420px 340px at 380px 250px, var(--photo-light) 0%, var(--photo-mid) 55%, transparent 100%),
      linear-gradient(180deg, #4d5a5e 0%, #56646a 55%, var(--bg-dark) 100%);
  }
  .study-request {
    position: absolute;
    left: 41px;
    top: 54px;
    color: var(--white);
    font-family: "Open Sans", Arial, sans-serif;
  }
  .study-request .kicker {
    margin: 0;
    font-size: 21px;
    font-weight: 400;
    line-height: 1.2;
  }
  .study-request .subject {
    margin: 4px 0 0;
    font-size: 24px;
    font-weight: 600;
    line-height: 35px;
    text-transform: uppercase;
  }
  .headline {
    position: absolute;
    left: 44px;
    top: 218px;
    margin: 0;
    font-family: "Oswald", Impact, sans-serif;
    font-weight: 700;
    font-size: 66px;
    line-height: 71px;
    letter-spacing: 5px;
    color: var(--white);
    text-transform: uppercase;
    text-shadow: 2px 3px 6px rgba(0,0,0,0.45);
  }
  .headline .accent { color: var(--orange); }
  .criteria {
    position: absolute;
    left: 100px;
    top: 598px;
    margin: 0;
    padding: 0;
    list-style: none;
    font-family: "Oswald", Impact, sans-serif;
    font-weight: 500;
    font-size: 23px;
    line-height: 33px;
    letter-spacing: 1.4px;
    color: var(--bullet-text);
    text-transform: uppercase;
    width: 760px;
  }
  .criteria li {
    position: relative;
    padding-left: 22px;
    margin-bottom: 1px;
  }
  .criteria li::before {
    content: "";
    position: absolute;
    left: 0;
    top: 13px;
    width: 9px;
    height: 9px;
    border-radius: 50%;
    background: #8d8d84;
  }
  .details {
    position: absolute;
    left: 64px;
    top: 816px;
    width: 830px;
    color: var(--body-text);
    font-size: 13px;
    line-height: 19px;
  }
  .details p { margin: 0 0 15px; }
  .details .highlight { color: var(--orange); }
  .details .credits { margin: 0; }
  .details strong { font-weight: 700; }
  .tear-offs {
    position: absolute;
    left: 0;
    top: 1000px;
    width: 927px;
    height: 200px;
    display: flex;
    padding-left: 24px;
    box-sizing: border-box;
  }
  .tab {
    position: relative;
    width: 70px;
    height: 200px;
    border-right: 1px solid var(--tab-line);
    box-sizing: border-box;
  }
  .tab:last-child { border-right: none; }
  .tab-text {
    position: absolute;
    left: 6px;
    bottom: 14px;
    transform-origin: left bottom;
    transform: rotate(-90deg) translate(0, 100%);
    white-space: nowrap;
    font-size: 14px;
    line-height: 18px;
  }
  .tab-text .study { color: var(--teal); display: block; }
  .tab-text .phone { color: #d8d8d0; display: block; }
  .tab-icon {
    position: absolute;
    left: 34px;
    top: 18px;
    width: 22px;
    height: 22px;
  }
</style>
</head>
<body>
<main class="flyer">
  <div class="hero-photo" role="img" aria-label="Photograph of a seated young woman holding a knife while a man's hand grips a belt beside her, against a grey wall"></div>

  <header class="study-request">
    <p class="kicker">Request for &nbsp;Study Participants</p>
    <p class="subject">Efficiency of Resources<br>Available to Suvivors of<br>Intimate Partner Abuse</p>
  </header>

  <h1 class="headline">Perceived<br>Effectiveness of<br><span class="accent">Domestic Violence</span><br>Services</h1>

  <ul class="criteria">
    <li>Are you eighteen years of age or older?</li>
    <li>Have you been a victim of domestic violence?</li>
    <li>Have you sought assistance with abuse in the last 12 months?</li>
    <li>Are you still in contact with the person who abused you?</li>
    <li>Are you willing and open to discussing your experience with abuse and your attempts to access services or resources?</li>
  </ul>

  <section class="details">
    <p>If you answered yes to all of these questions, you may be eligible t participate in a study to better understand the resources needed and services expected for survivors of domestic violence.</p>
    <p>Plese contact Dana Whitfield at <span class="highlight">1(773)555-0148</span> or via e-mail <span class="highlight">survivorstudy@examplemail.com</span> for additional information. Participants will be compensated for their time.</p>
    <p class="credits"><strong>Principal Investigator:</strong> Dana Whitfield<br>
    <strong>Institutional Addiliation:</strong> Lakeshore State University, Dept. of Criminology,Law, and Justice<br>
    <strong>Contact Address:</strong> Post Office Box 210455, Chicago, IL 60601</p>
  </section>

  <footer class="tear-offs">
    <div class="tab"><div class="tab-text"><span class="study">Survivor Resources Study</span><span class="phone">1(773)555-0148</span></div><svg class="tab-icon" viewBox="0 0 22 22"><circle cx="11" cy="11" r="8" fill="none" stroke="#ee6a2c" stroke-width="5"/><circle cx="11" cy="11" r="8" fill="none" stroke="#fff" stroke-width="5" stroke-dasharray="6.3 6.3"/></svg></div>
    <div class="tab"><div class="tab-text"><span class="study">Survivor Resources Study</span><span class="phone">1(773)555-0148</span></div><svg class="tab-icon" viewBox="0 0 22 22"><circle cx="11" cy="11" r="8" fill="none" stroke="#ee6a2c" stroke-width="5"/><circle cx="11" cy="11" r="8" fill="none" stroke="#fff" stroke-width="5" stroke-dasharray="6.3 6.3"/></svg></div>
    <div class="tab"><div class="tab-text"><span class="study">Survivor Resources Study</span><span class="phone">1(773)555-0148</span></div><svg class="tab-icon" viewBox="0 0 22 22"><circle cx="11" cy="11" r="8" fill="none" stroke="#ee6a2c" stroke-width="5"/><circle cx="11" cy="11" r="8" fill="none" stroke="#fff" stroke-width="5" stroke-dasharray="6.3 6.3"/></svg></div>
    <div class="tab"><div class="tab-text"><span class="study">Survivor Resources Study</span><span class="phone">1(773)555-0148</span></div><svg class="tab-icon" viewBox="0 0 22 22"><circle cx="11" cy="11" r="8" fill="none" stroke="#ee6a2c" stroke-width="5"/><circle cx="11" cy="11" r="8" fill="none" stroke="#fff" stroke-width="5" stroke-dasharray="6.3 6.3"/></svg></div>
    <div class="tab"><div class="tab-text"><span class="study">Survivor Resources Study</span><span class="phone">1(773)555-0148</span></div><svg class="tab-icon" viewBox="0 0 22 22"><circle cx="11" cy="11" r="8" fill="none" stroke="#ee6a2c" stroke-width="5"/><circle cx="11" cy="11" r="8" fill="none" stroke="#fff" stroke-width="5" stroke-dasharray="6.3 6.3"/></svg></div>
    <div class="tab"><div class="tab-text"><span class="study">Survivor Resources Study</span><span class="phone">1(773)555-0148</span></div><svg class="tab-icon" viewBox="0 0 22 22"><circle cx="11" cy="11" r="8" fill="none" stroke="#ee6a2c" stroke-width="5"/><circle cx="11" cy="11" r="8" fill="none" stroke="#fff" stroke-width="5" stroke-dasharray="6.3 6.3"/></svg></div>
    <div class="tab"><div class="tab-text"><span class="study">Survivor Resources Study</span><span class="phone">1(773)555-0148</span></div><svg class="tab-icon" viewBox="0 0 22 22"><circle cx="11" cy="11" r="8" fill="none" stroke="#ee6a2c" stroke-width="5"/><circle cx="11" cy="11" r="8" fill="none" stroke="#fff" stroke-width="5" stroke-dasharray="6.3 6.3"/></svg></div>
    <div class="tab"><div class="tab-text"><span class="study">Survivor Resources Study</span><span class="phone">1(773)555-0148</span></div><svg class="tab-icon" viewBox="0 0 22 22"><circle cx="11" cy="11" r="8" fill="none" stroke="#ee6a2c" stroke-width="5"/><circle cx="11" cy="11" r="8" fill="none" stroke="#fff" stroke-width="5" stroke-dasharray="6.3 6.3"/></svg></div>
    <div class="tab"><div class="tab-text"><span class="study">Survivor Resources Study</span><span class="phone">1(773)555-0148</span></div><svg class="tab-icon" viewBox="0 0 22 22"><circle cx="11" cy="11" r="8" fill="none" stroke="#ee6a2c" stroke-width="5"/><circle cx="11" cy="11" r="8" fill="none" stroke="#fff" stroke-width="5" stroke-dasharray="6.3 6.3"/></svg></div>
    <div class="tab"><div class="tab-text"><span class="study">Survivor Resources Study</span><span class="phone">1(773)555-0148</span></div><svg class="tab-icon" viewBox="0 0 22 22"><circle cx="11" cy="11" r="8" fill="none" stroke="#ee6a2c" stroke-width="5"/><circle cx="11" cy="11" r="8" fill="none" stroke="#fff" stroke-width="5" stroke-dasharray="6.3 6.3"/></svg></div>
    <div class="tab"><div class="tab-text"><span class="study">Survivor Resources Study</span><span class="phone">1(773)555-0148</span></div><svg class="tab-icon" viewBox="0 0 22 22"><circle cx="11" cy="11" r="8" fill="none" stroke="#ee6a2c" stroke-width="5"/><circle cx="11" cy="11" r="8" fill="none" stroke="#fff" stroke-width="5" stroke-dasharray="6.3 6.3"/></svg></div>
    <div class="tab"><div class="tab-text"><span class="study">Survivor Resources Study</span><span class="phone">1(773)555-0148</span></div><svg class="tab-icon" viewBox="0 0 22 22"><circle cx="11" cy="11" r="8" fill="none" stroke="#ee6a2c" stroke-width="5"/><circle cx="11" cy="11" r="8" fill="none" stroke="#fff" stroke-width="5" stroke-dasharray="6.3 6.3"/></svg></div>
    <div class="tab"><div class="tab-text"><span class="study">Survivor Resources Study</span><span class="phone">1(773)555-0148</span></div><svg class="tab-icon" viewBox="0 0 22 22"><circle cx="11" cy="11" r="8" fill="none" stroke="#ee6a2c" stroke-width="5"/><circle cx="11" cy="11" r="8" fill="none" stroke="#fff" stroke-width="5" stroke-dasharray="6.3 6.3"/></svg></div>
  </footer>
</main>
</body>
</html>
```